Lodgevo and Small Event Venue Site

Looking for a basic site that would also include a seperate landing page for our email list. We have rehabbed an old 1905 Bank Building into a Lodgevo /Small Event Venue (baby showers, birthday parties, mixers, etc) . We are looking for an very nice professional page along with integration with the Lodgevo Booking Calendar. We have a nice logo we can provide you with......The Name Of Our Venue is "The Ivy Lantern Hall".

```html
<!DOCTYPE html>
<html lang="en">
<head>
<meta charset="utf-8">
<title>The Ivy Lantern Hall</title>
<link href="https://fonts.googleapis.com/css2?family=Righteous&family=Poppins:wght@400;500;600&display=swap" rel="stylesheet">
<style>
:root{
  --orange:#f2a94a;
  --black:#000;
  --white:#fff;
  --ink:#111;
  --field:#4a4a4a;
  --muted:#8a8a8a;
}
*{margin:0;padding:0;box-sizing:border-box}
html,body{width:1200px;height:4461px;overflow:hidden}
body{position:relative;background:var(--white);font-family:"Poppins",sans-serif;color:var(--ink)}
.abs{position:absolute}
.display{font-family:"Righteous",sans-serif;letter-spacing:2px}
.accent{color:var(--orange)}
.btn{position:absolute;background:var(--orange);color:var(--ink);border-radius:30px;display:flex;align-items:center;justify-content:center;font-family:"Righteous",sans-serif;letter-spacing:1.5px}
.section-title{position:absolute;left:0;width:1200px;text-align:center;font-family:"Righteous",sans-serif;font-size:40px;letter-spacing:3px;transform:translateY(-50%)}

/* header */
.brand{position:absolute;display:flex;align-items:center;gap:10px;font-family:"Righteous",sans-serif;font-size:30px;letter-spacing:1px}
.brand-mark{width:40px;height:40px;border:4px solid currentColor;border-radius:4px}
.nav{position:absolute;display:flex;gap:40px;font-size:17px;font-weight:500}

/* hero */
.hero{position:absolute;left:0;top:99px;width:1200px;height:545px;background:linear-gradient(160deg,#7a2f22 0%,#9b4433 38%,#5d7fbf 62%,#4a7bd6 100%)}
.hero-box{position:absolute;left:326px;top:182px;width:549px;height:294px;background:rgba(0,0,0,.78);border-radius:16px;color:var(--white);text-align:center}
.hero-box h1{font-family:"Righteous",sans-serif;font-weight:400;font-size:40px;letter-spacing:3px;margin-top:40px}
.hero-box p{font-size:15px;line-height:34px;margin-top:12px}

/* about */
.about-photo{position:absolute;left:155px;top:743px;width:394px;height:394px;border-radius:50%;background:radial-gradient(circle at 45% 45%,#e9c28e,#b96a4c 60%,#7a4d3a);border:3px solid #6b4a2a}
.about-text{position:absolute;left:597px;top:772px;width:482px;font-size:16px;line-height:33.6px;text-align:justify;text-align-last:justify}

/* newsletter */
.newsletter{position:absolute;left:0;top:1226px;width:1200px;height:385px;background:var(--black);color:var(--white);text-align:center}
.newsletter h2{font-family:"Righteous",sans-serif;font-weight:400;font-size:40px;letter-spacing:3px;margin-top:68px}
.newsletter p{font-size:15.5px;line-height:34px;margin-top:20px}
.signup{position:absolute;left:355px;top:253px;width:490px;height:54px;background:var(--white);border-radius:30px;text-align:left}
.signup span{position:absolute;left:22px;top:17px;font-size:15px;color:#666}
.signup .btn{left:300px;top:0;width:190px;height:54px;font-size:22px}

/* services */
.card{position:absolute;top:1796px;width:316px;height:389px;border-radius:12px}
.card-label{position:absolute;top:2142px;width:259px;height:75px;background:var(--white);box-shadow:0 4px 8px rgba(0,0,0,.25);display:flex;align-items:center;justify-content:center;font-family:"Righteous",sans-serif;font-size:25px;letter-spacing:2px}
.arrow{position:absolute;top:1971px;width:40px;height:40px;border-radius:50%;background:var(--black)}

/* calendar */
.cal-btn{top:2395px;width:158px;height:49px;font-size:17px}
.month{position:absolute;left:500px;top:2400px;width:200px;text-align:center;font-family:"Righteous",sans-serif;font-size:25px;letter-spacing:1px}
.cal-cell{position:absolute;width:80px;margin-left:-40px;text-align:center;transform:translateY(-50%);font-size:15px}
.cal-head{font-family:"Righteous",sans-serif;font-size:25px;letter-spacing:2px}
.cal-cell.today{color:var(--orange)}
.cal-cell.next{color:var(--muted)}

/* contact */
.contact{position:absolute;left:0;top:2871px;width:1200px;height:599px;background:var(--black)}
.contact-photo{position:absolute;left:0;top:0;width:1200px;height:599px}
.contact h2{position:absolute;left:68px;width:488px;top:28px;text-align:center;color:var(--white);font-family:"Righteous",sans-serif;font-weight:400;font-size:34px;letter-spacing:3px}
.field{position:absolute;left:68px;width:488px;background:var(--field);color:var(--white);font-size:15px;padding:20px 0 0 45px}
.contact .btn{left:234px;top:508px;width:157px;height:50px;font-size:17px}

/* team */
.member{position:absolute;top:3647px;width:266px;height:266px;border-radius:50%}
.member-name{position:absolute;top:3962px;width:266px;text-align:center;font-size:24px}
.dot{position:absolute;width:42px;height:42px;border-radius:50%}

/* footer */
.footer{position:absolute;left:0;top:4061px;width:1200px;height:400px;background:var(--black);color:var(--white)}
.footer .nav{left:0;width:1200px;justify-content:center;top:232px}
.copyright{position:absolute;left:0;width:1200px;top:366px;text-align:center;font-size:16px}
</style>
</head>
<body>

<!-- header -->
<header>
  <div class="brand" style="left:110px;top:30px;color:#444">
    <span class="brand-mark"></span>The Ivy Lantern Hall
  </div>
  <nav class="nav" style="left:508px;top:40px">
    <span>Home</span><span>About Us</span><span>Lodgevo Booking Calendar</span><span>Contact Us</span>
  </nav>
</header>

<!-- hero -->
<section class="hero" role="img" aria-label="Red brick facade of the restored 1905 bank building under a blue sky"></section>
<svg class="abs" style="left:0;top:560px" width="1200" height="90" viewBox="0 0 1200 90">
  <path d="M0 85 Q560 -30 1200 20 V90 H0 Z" fill="var(--white)"/>
  <path d="M0 85 Q560 -30 1200 20" fill="none" stroke="var(--orange)" stroke-width="7"/>
</svg>
<div class="hero-box">
  <h1>The Ivy Lantern Hall</h1>
  <p>Lorem ipsum dolor sit amet, consectetur adipiscing elit,<br>sed do eiusmod tempor incididunt ut labore et dolore</p>
  <div class="btn" style="left:167px;top:197px;width:215px;height:54px;font-size:23px">GET STARTED</div>
</div>

<!-- about -->
<h2 class="section-title" style="top:684px">ABOUT <span class="accent">US</span></h2>
<div class="about-photo" role="img" aria-label="Children blowing out candles on a birthday cake"></div>
<p class="about-text">Sed ut perspiciatis unde omnis iste natus error sit voluptatem accusantium doloremque laudantium, totam rem aperiam, eaque ipsa quae ab illo inventore veritatis et quasi architecto beatae vitae dicta sunt explicabo. Nemo enim ipsam voluptatem quia voluptas sit aspernatur aut odit aut fugit, sed quia consequuntur magni dolores eos qui ratione voluptatem sequi nesciunt. Neque porro quisquam</p>
<div class="btn" style="left:597px;top:1042px;width:217px;height:54px;font-size:22px">LEARN MORE</div>

<!-- newsletter -->
<section class="newsletter">
  <h2>SUBSCRIBE <span class="accent">TO OUR</span> NEWSLETTER</h2>
  <p>Sed ut perspiciatis unde omnis iste natus error sit voluptatem accusantium doloremque<br>laudantium, totam rem aperiam, eaque ipsa quae ab illo inventore veritatis et quasi</p>
  <div class="signup"><span>Enter Your Email Address</span><div class="btn">SIGN UP</div></div>
</section>

<!-- services -->
<h2 class="section-title" style="top:1713px">OUR <span class="accent">SERVICES</span></h2>
<div class="arrow" style="left:60px"><svg width="40" height="40" viewBox="0 0 40 40"><path d="M23 12 L15 20 L23 28" fill="none" stroke="#fff" stroke-width="3"/></svg></div>
<div class="arrow" style="left:1097px"><svg width="40" height="40" viewBox="0 0 40 40"><path d="M17 12 L25 20 L17 28" fill="none" stroke="#fff" stroke-width="3"/></svg></div>
<div class="card" style="left:111px;background:linear-gradient(170deg,#d9d4cc,#8d7462 60%,#3d2f2a)" role="img" aria-label="Guests celebrating at a baby shower with balloons"></div>
<div class="card" style="left:441px;background:radial-gradient(circle at 50% 45%,#f0b650,#7b5a3a 45%,#3b3433)" role="img" aria-label="Birthday cake with lit candles"></div>
<div class="card" style="left:771px;background:linear-gradient(160deg,#7b4a6a,#c98aa0 45%,#5a2a3a)" role="img" aria-label="Friends dancing under falling confetti at a mixer"></div>
<div class="card-label" style="left:139px">BABY SHOWERS</div>
<div class="card-label" style="left:470px">BIRTHDAY PARTIES</div>
<div class="card-label" style="left:800px">MIXERS</div>

<!-- calendar -->
<h2 class="section-title" style="top:2317px">BOOK <span class="accent">AN</span> APPOINTMENT</h2>
<div class="btn cal-btn" style="left:327px">PREVIOUS</div>
<div class="month">OCT 2023</div>
<div class="btn cal-btn" style="left:722px">NEXT</div>

<div class="cal-cell cal-head" style="left:286px;top:2497px">SUN</div>
<div class="cal-cell cal-head" style="left:393px;top:2497px">MON</div>
<div class="cal-cell cal-head" style="left:500px;top:2497px">TUE</div>
<div class="cal-cell cal-head" style="left:610px;top:2497px">WED</div>
<div class="cal-cell cal-head" style="left:713px;top:2497px">THU</div>
<div class="cal-cell cal-head" style="left:814px;top:2497px">FRI</div>
<div class="cal-cell cal-head" style="left:913px;top:2497px">SAT</div>

<div class="cal-cell" style="left:286px;top:2560px">01</div><div class="cal-cell" style="left:393px;top:2560px">02</div><div class="cal-cell" style="left:500px;top:2560px">03</div><div class="cal-cell" style="left:610px;top:2560px">04</div><div class="cal-cell" style="left:720px;top:2560px">05</div><div class="cal-cell" style="left:814px;top:2560px">06</div><div class="cal-cell" style="left:913px;top:2560px">07</div>
<div class="cal-cell" style="left:286px;top:2615px">08</div><div class="cal-cell" style="left:393px;top:2615px">09</div><div class="cal-cell" style="left:500px;top:2615px">10</div><div class="cal-cell today" style="left:610px;top:2615px">11</div><div class="cal-cell" style="left:720px;top:2615px">12</div><div class="cal-cell" style="left:814px;top:2615px">13</div><div class="cal-cell" style="left:913px;top:2615px">14</div>
<div class="cal-cell" style="left:286px;top:2670px">15</div><div class="cal-cell" style="left:393px;top:2670px">16</div><div class="cal-cell" style="left:500px;top:2670px">17</div><div class="cal-cell" style="left:610px;top:2670px">18</div><div class="cal-cell" style="left:720px;top:2670px">19</div><div class="cal-cell" style="left:814px;top:2670px">20</div><div class="cal-cell" style="left:913px;top:2670px">21</div>
<div class="cal-cell" style="left:286px;top:2724px">22</div><div class="cal-cell" style="left:393px;top:2724px">23</div><div class="cal-cell" style="left:500px;top:2724px">24</div><div class="cal-cell" style="left:610px;top:2724px">25</div><div class="cal-cell" style="left:720px;top:2724px">26</div><div class="cal-cell" style="left:814px;top:2724px">27</div><div class="cal-cell" style="left:913px;top:2724px">28</div>
<div class="cal-cell" style="left:286px;top:2779px">29</div><div class="cal-cell" style="left:393px;top:2779px">30</div><div class="cal-cell" style="left:500px;top:2779px">31</div><div class="cal-cell next" style="left:610px;top:2779px">01</div><div class="cal-cell next" style="left:720px;top:2779px">02</div><div class="cal-cell next" style="left:814px;top:2779px">03</div><div class="cal-cell next" style="left:913px;top:2779px">04</div>

<!-- contact -->
<section class="contact">
  <svg class="contact-photo" width="1200" height="599" viewBox="0 0 1200 599" role="img" aria-label="Friends celebrating with a birthday cake, sparklers and party hats">
    <defs>
      <linearGradient id="party" x1="0" y1="0" x2="1" y2="1">
        <stop offset="0" stop-color="#6d6a72"/>
        <stop offset=".45" stop-color="#b8643a"/>
        <stop offset="1" stop-color="#2e2a3a"/>
      </linearGradient>
    </defs>
    <path d="M684 0 H1200 V599 H610 Z" fill="url(#party)"/>
  </svg>
  <h2>CONTACT US</h2>
  <div class="field" style="top:97px;height:63px">FULL NAME</div>
  <div class="field" style="top:187px;height:63px">EMAIL ADDRESS</div>
  <div class="field" style="top:279px;height:62px">PHONE NUMBER</div>
  <div class="field" style="top:373px;height:97px">TYPE YOUR MESSAGE HERE....</div>
  <div class="btn">SUBMIT</div>
</section>

<!-- team -->
<h2 class="section-title" style="top:3567px;color:#333">OUR <span class="accent">TEAM</span></h2>
<div class="member" style="left:142px;background:#e6e6e6" role="img" aria-label="Team member portrait"></div>
<div class="member" style="left:464px;background:#3fb1d1" role="img" aria-label="Team member portrait"></div>
<div class="member" style="left:790px;background:#e3c3cf" role="img" aria-label="Team member portrait"></div>
<div class="member-name" style="left:142px">Lorem ipsum</div>
<div class="member-name" style="left:464px">Lorem ipsum</div>
<div class="member-name" style="left:790px">Lorem ipsum</div>
<div class="dot" style="left:221px;top:4012px;background:#3b5ba6"></div><div class="dot" style="left:291px;top:4012px;background:#d9368a"></div>
<div class="dot" style="left:543px;top:4012px;background:#3b5ba6"></div><div class="dot" style="left:613px;top:4012px;background:#d9368a"></div>
<div class="dot" style="left:869px;top:4012px;background:#3b5ba6"></div><div class="dot" style="left:939px;top:4012px;background:#d9368a"></div>

<!-- footer -->
<footer class="footer">
  <svg class="abs" style="left:0;top:0" width="1200" height="100" viewBox="0 0 1200 100">
    <path d="M0 0 H1200 V4 Q600 150 0 4 Z" fill="var(--white)"/>
    <path d="M0 14 Q600 150 1200 14" fill="none" stroke="var(--orange)" stroke-width="6"/>
  </svg>
  <div class="brand" style="left:0;width:1200px;justify-content:center;top:157px;color:#ccc">
    <span class="brand-mark"></span>The Ivy Lantern Hall
  </div>
  <nav class="nav"><span>Home</span><span>About Us</span><span>Lodgevo Booking Calendar</span><span>Contact Us</span></nav>
  <div class="dot" style="left:545px;top:292px;background:#3b5ba6"></div>
  <div class="dot" style="left:615px;top:292px;background:#d9368a"></div>
  <p class="copyright">@COPYRIGHTS 2023. THE IVY LANTERN HALL. ALL RIGHTS RESERVED.</p>
</footer>

</body>
</html>
```